Purl Haven planner/ book cover

PURL HAVEN" - A UNIQUE NOTEBOOK FOR CRAFTS. The main goal of a "Purl Haven" notebook is to arrange your crafts notes like knitting planner. Its pages are systematically structured, so they are easy to review, and all the information about the started project is in one place. The notebook has a click opening system, so you can remove, insert, change pages.
This is the old design in Latvian language. I want a new, classic, modern cover design for selling book in USA.I prefer original picture rather than download. Maybe for some of yourself drawings. Illustrated color-wash and minimalistic style better than photography.
Look at the pages inside design so that the lid fits. Maybe i want to change some clipart on the inside as well (just small one, like ball of yarn, sweater, can be seen in the picture, more classic style, not so childish, but that's latter), leave yoga clipart and the colors. Check please video.
https://www.examplevideo-host.com/watch?v=Qm4rT8zLk2W
www.purlhavenstudio.com its my style.

book title- purl haven
slogan- its time for sitting to do some knitting
size- 18 x 23,5 x 4 cm

Colors
d3a5cc
eea4c8
fdf2f7
fbd4d5
fdf0f6
ffffff
e34297
a64599
b868aa

```html
<!DOCTYPE html>
<html lang="en">
<head>
<meta charset="utf-8">
<title>Purl Haven – Cover and Planner Pages</title>
<link rel="stylesheet" href="https://fonts.googleapis.com/css2?family=Amatic+SC:wght@400;700&family=Dancing+Script:wght@600;700&display=swap">
<style>
  :root{
    --stage-top:#c8c8c8;
    --stage-bottom:#f6eef1;
    --wash-strong:#eea4c8;
    --wash-soft:#fbd4d5;
    --wash-pale:#fdf0f6;
    --paper:#ffffff;
    --title-plum:#6e1748;
    --heading-rose:#b4485f;
    --body-violet:#a64599;
    --line-rose:#e07a91;
    --grid-rose:#df6e86;
    --ink:#2a2226;
    --yarn:#c9b3b1;
    --wood:#c9a77c;
    --figure:#ece6e8;
  }
  *{margin:0;padding:0;box-sizing:border-box}
  html,body{width:1200px;height:3053px;overflow:hidden}
  body{position:relative;background:var(--stage-bottom);font-family:"Amatic SC",cursive}
  .stage-cover{position:absolute;left:0;top:0;width:1200px;height:1118px;background:var(--stage-top)}
  .abs{position:absolute}

  /* cover */
  .cover{left:320px;top:89px;width:616px;height:942px;overflow:hidden;
    background:
      radial-gradient(ellipse 60% 22% at 55% 30%, rgba(238,164,200,.55), transparent 70%),
      radial-gradient(ellipse 70% 25% at 50% 62%, rgba(251,212,213,.7), transparent 70%),
      linear-gradient(180deg,var(--wash-soft) 0%,var(--wash-pale) 45%,var(--paper) 75%,var(--wash-soft) 100%);
    box-shadow:0 6px 18px rgba(0,0,0,.18)}
  .cover-title-small{left:0;width:616px;top:98px;padding-left:270px;font-family:"Dancing Script",cursive;font-weight:700;font-size:58px;color:var(--title-plum);line-height:1}
  .cover-title-main{left:0;width:616px;top:140px;text-align:center;font-family:"Dancing Script",cursive;font-weight:700;font-size:142px;color:var(--title-plum);line-height:1.1}
  .cover-slogan{left:0;width:616px;top:806px;text-align:center;font-size:36px;font-weight:700;color:var(--ink);letter-spacing:.5px}

  /* planner pages */
  .page{overflow:hidden;
    background:
      radial-gradient(ellipse 45% 30% at 20% 50%, rgba(251,212,213,.55), transparent 70%),
      linear-gradient(180deg,var(--wash-strong) 0%,var(--wash-soft) 12%,var(--paper) 30%,var(--paper) 72%,var(--wash-soft) 88%,var(--wash-strong) 100%);
    box-shadow:0 2px 8px rgba(0,0,0,.08)}
  .page-heading{text-align:center;color:var(--heading-rose);font-size:30px;line-height:1.2}
  .page-body{text-align:center;color:var(--body-violet);font-size:27px;line-height:1.22}
  .field{display:flex;align-items:flex-end;gap:8px;color:var(--heading-rose);font-size:17px}
  .field svg{flex:none}
  .field-label{width:64px}
  .field-line{flex:1;border-bottom:1px solid var(--line-rose);height:14px}
  .note{color:var(--heading-rose);font-size:13px;line-height:14px}
</style>
</head>
<body>
  <div class="stage-cover"></div>

  <!-- Cover -->
  <section class="cover abs">
    <div class="cover-title-small abs">purl</div>
    <div class="cover-title-main abs">Haven</div>
    <svg class="abs" style="left:0;top:0" width="616" height="942" viewBox="0 0 616 942">
      <path role="img" aria-label="Photo of yarn balls in a heart-shaped basket"
        d="M243 430 C210 360 120 350 95 400 C70 455 110 540 240 690 C370 540 410 455 385 400 C360 350 275 360 243 430 Z"
        fill="var(--yarn)" stroke="#b49575" stroke-width="6"/>
      <g role="img" aria-label="Pair of wooden knitting needles">
        <line x1="272" y1="764" x2="498" y2="382" stroke="var(--wood)" stroke-width="8" stroke-linecap="round"/>
        <line x1="300" y1="770" x2="560" y2="470" stroke="var(--wood)" stroke-width="8" stroke-linecap="round"/>
      </g>
    </svg>
    <div class="cover-slogan abs">Its time for sitting to do some knitting</div>
  </section>

  <!-- Spread 1 -->
  <section class="page abs" style="left:146px;top:1325px;width:441px;height:636px">
    <div class="page-heading abs" style="left:0;width:441px;top:97px">Lorem Ipsum Simply Dummy Text</div>
    <div class="page-body abs" style="left:0;width:441px;top:236px">Lorem Ipsum is simply<br>dummy text of the printing<br>and typesetting industry.</div>
    <svg class="abs" style="left:195px;top:343px" width="50" height="10"><path d="M2 5 Q12 0 25 5 Q38 10 48 5" fill="none" stroke="var(--line-rose)" stroke-width="1.5"/></svg>
    <div class="page-body abs" style="left:0;width:441px;top:372px">Lorem Ipsum has been the<br>industry's standard dummy text<br>ever since the 1500s,</div>
  </section>

  <section class="page abs" style="left:598px;top:1325px;width:474px;height:636px">
    <svg class="abs" style="left:0;top:0" width="474" height="636">
      <polygon points="80,172 385,150 408,445 100,488" fill="none" stroke="var(--line-rose)" stroke-width="1.2"/>
      <polygon points="72,198 380,168 372,480 88,470" fill="none" stroke="var(--line-rose)" stroke-width="1.2"/>
    </svg>
    <div class="page-heading abs" style="left:0;width:486px;top:226px;font-size:28px">Lorem Ipsum Simply<br>Dummy Text</div>
    <div class="abs" style="left:103px;top:312px;width:262px;display:flex;flex-direction:column;gap:17px">
      <div class="field"><svg width="16" height="14"><path d="M1 7 L15 1 L11 13 L7 8 Z M7 8 L15 1" fill="none" stroke="var(--heading-rose)" stroke-width="1.2"/></svg><span class="field-label">Message</span><span class="field-line"></span></div>
      <div class="field"><svg width="16" height="14"><path d="M3 1 L6 1 L7 4 L5 6 Q7 9 10 10 L12 8 L15 9 L15 12 Q10 14 5 9 Q1 5 3 1 Z" fill="none" stroke="var(--heading-rose)" stroke-width="1.2"/></svg><span class="field-label">Telephone</span><span class="field-line"></span></div>
      <div class="field"><svg width="16" height="14"><rect x="1" y="2" width="14" height="10" fill="none" stroke="var(--heading-rose)" stroke-width="1.2"/><path d="M1 2 L8 8 L15 2" fill="none" stroke="var(--heading-rose)" stroke-width="1.2"/></svg><span class="field-label">E-mail</span><span class="field-line"></span></div>
      <div class="field"><svg width="16" height="14"><path d="M8 13 Q2 7 2 5 A6 4.5 0 0 1 14 5 Q14 7 8 13 Z" fill="none" stroke="var(--heading-rose)" stroke-width="1.2"/><circle cx="8" cy="5" r="2" fill="none" stroke="var(--heading-rose)" stroke-width="1.2"/></svg><span class="field-label">Address</span><span class="field-line"></span></div>
    </div>
  </section>

  <!-- Spread 2 -->
  <section class="page abs" style="left:152px;top:2228px;width:429px;height:634px">
    <div class="page-heading abs" style="left:0;width:429px;top:94px;font-size:32px">Lorem Ipsum Simply<br>Dummy Text</div>
    <svg class="abs" style="left:49px;top:225px" width="334" height="298">
      <g fill="none" stroke="var(--grid-rose)" stroke-width="1.3">
        <rect x="1" y="1" width="332" height="296" fill="#fff"/>
        <path d="M56 1V297M111 1V297M166 1V297M221 1V297M277 1V297"/>
        <path d="M1 30H333M1 60H333M1 89H333M1 119H333M1 148H333M1 178H333M1 207H333M1 237H333M1 267H333"/>
      </g>
    </svg>
  </section>

  <section class="page abs" style="left:598px;top:2228px;width:465px;height:634px">
    <div class="abs" role="img" aria-label="Line drawing of a body outline for taking measurements" style="left:99px;top:41px;width:85px;height:172px;background:var(--figure);border-radius:40px 40px 10px 10px"></div>
    <p class="note abs" style="left:225px;top:71px;width:188px">Lorem Ipsum is simply dummy text of the printing and typesetting industry. Lorem Ipsum has been the industry's standard dummy text ever since the 1500s, when an unknown printer took a galley of type and scrambled it to make a type specimen book. It has survived not only five centuries,</p>
    <svg class="abs" style="left:59px;top:219px" width="360" height="304">
      <g fill="none" stroke="var(--grid-rose)" stroke-width="1.3">
        <rect x="1" y="1" width="358" height="302" fill="#fff"/>
        <path d="M61 1V303M120 1V303M180 1V303M240 1V303M299 1V303"/>
        <path d="M1 26H359M1 51H359M1 76H359M1 101H359M1 126H359M1 151H359M1 176H359M1 201H359M1 226H359M1 251H359M1 277H359"/>
      </g>
    </svg>
  </section>
</body>
</html>
```